nine-parts.com

We are a small dollar lending company that will revolutionize the industry. We will do this by being completely transparent, fee free, etc and an interest rate that normal people can afford to pay. Over 10X less than our competition. We only allow our members to pay bills " bills paid fast", within 72 hours. Payday loans typically charge from 390%-600% with a terrible payback structure. We charge 36%, period, with a payback structure over 12 months. Our site will be very simple and easy to use but elegant at the same time. We do not want the site to be too busy, less is more and easier. We will have; Home, The Story, Why 9parts.com, Are you eligible? Members, Clients. To become a member you have to be referred by a current client of 9parts.com. A lot of the busy stuff will be saved for the Members and Clients sections. The feel must be elegant, easy to use and very simple to understand. I am looking for the green, white and black combinations of colors, very similar to my logo that was designed by Pixelmoor.

```html
<!DOCTYPE html>
<html lang="en">
<head>
<meta charset="utf-8">
<title>nine-parts.com — Bills Paid Fast</title>
<link rel="stylesheet" href="https://fonts.googleapis.com/css2?family=Open+Sans:wght@300;400;600;700&family=Oswald:wght@400&display=swap">
<style>
:root{
  --green:#9bdd7e;
  --green-text:#4cb84a;
  --green-dark:#3d9a3b;
  --charcoal:#454545;
  --charcoal-deep:#3a3a3a;
  --paper:#f7f7f7;
  --white:#ffffff;
  --ink:#444444;
  --muted:#7a7a7a;
  --rule:#dddddd;
  --ribbon:#fcc93a;
}
*{margin:0;padding:0;box-sizing:border-box}
html,body{width:997px;height:1200px;overflow:hidden}
body{font-family:"Open Sans",Arial,sans-serif;background:var(--paper);color:var(--ink);position:relative}
.abs{position:absolute}

.site-header{left:0;top:0;width:997px;height:78px;background:var(--green)}
.brand{left:137px;top:6px;font-family:"Oswald",sans-serif;font-size:35px;color:var(--white);letter-spacing:-0.5px;line-height:1.1}
.tagline{left:172px;top:44px;font-size:16px;color:#23401f;letter-spacing:.3px}
.contact-card{left:578px;top:12px;width:278px;height:55px;background:var(--white);box-shadow:0 3px 6px rgba(0,0,0,.2)}
.contact-ribbon{left:607px;top:8px;width:222px;height:20px;background:var(--ribbon);color:var(--white);font-size:11.5px;font-weight:600;text-align:center;line-height:18px;clip-path:polygon(0 0,100% 0,96% 70%,50% 100%,4% 70%)}
.contact-line{left:594px;top:39px;font-size:15px;color:#555;white-space:nowrap}
.contact-line span{margin-right:8px}

.nav-band{left:0;top:78px;width:997px;height:137px;background:var(--charcoal)}
.main-nav{left:0;top:86px;width:997px;display:flex;justify-content:center;gap:29px;font-size:13px;font-weight:600;color:var(--white)}
.main-nav .current{color:var(--green)}

.hero{left:138px;top:116px;width:718px;height:209px;background:linear-gradient(120deg,#c9ced6 0%,#8d929c 35%,#50545c 55%,#b7a18e 75%,#d9dee5 100%)}

.welcome{left:138px;top:325px;width:718px;height:117px;background:linear-gradient(#fdfdfd,#f2f2f2)}
.welcome h1{position:absolute;left:0;width:100%;top:13px;text-align:center;font-weight:300;font-size:21px;color:#555}
.welcome h1 strong{font-weight:600;color:var(--green-text)}
.welcome p{position:absolute;left:11px;top:49px;width:697px;font-size:10.6px;line-height:17px;color:#555}
.welcome a{color:var(--green-text);font-weight:600;text-decoration:none;margin-left:6px}
.welcome-shadow{left:220px;top:441px;width:560px;height:10px;border-radius:50%;background:radial-gradient(ellipse at top,rgba(0,0,0,.25),rgba(0,0,0,0) 70%)}

.panel{left:138px;top:465px;width:718px;height:487px;background:rgba(255,255,255,.85);border:1px solid #e4e4e4;border-bottom:none}
.section-title{left:0;width:997px;text-align:center;font-weight:300;font-size:21px;color:#555}
.calc-field{top:521px;font-size:11.8px;font-weight:600;color:var(--green-text);white-space:nowrap}
.calc-hint{left:153px;top:536px;font-size:9.8px;color:#999}
.rule{left:153px;width:688px;height:1px;background:var(--rule)}
.calc-notes{left:153px;top:560px;width:688px;height:65px;background:linear-gradient(#fff,#f6f6f6);padding:7px 14px;font-size:10.3px;line-height:17px;color:#777}

.feature{width:290px}
.feature h3{display:flex;align-items:center;gap:7px;font-size:12.3px;font-weight:600;color:#444;margin-left:-1px}
.feature h3 svg{flex:none}
.feature p{margin-top:7px;font-size:10.3px;line-height:17px;color:#888;text-align:justify}

.payees{left:0;top:952px;width:997px;height:162px;background:var(--green);color:var(--white)}
.payees h2{position:absolute;left:0;width:100%;top:20px;text-align:center;font-weight:300;font-size:20px}
.payee-types{position:absolute;top:63px;left:0;width:100%;display:flex;justify-content:center;gap:42px;font-size:15px;font-weight:600}
.payee-types div{display:flex;align-items:center;gap:6px}
.payee-list{position:absolute;left:130px;top:110px;width:737px;text-align:center;font-size:10.4px;font-weight:600;line-height:17px}

.site-footer{left:0;top:1114px;width:997px;height:86px;background:var(--charcoal-deep);color:#ddd;text-align:center}
.footer-nav{position:absolute;top:12px;width:100%;font-size:12px;font-weight:600}
.copyright{position:absolute;top:32px;width:100%;font-size:12px;font-weight:600}
.social{position:absolute;top:55px;left:471px;display:flex;gap:4px}
.social span{width:16px;height:16px;border:1px solid #ccc;border-radius:50%}
</style>
</head>
<body>

<header class="abs site-header"></header>
<div class="abs brand">nine-parts.com</div>
<div class="abs tagline">"Bills Paid Fast"</div>
<div class="abs contact-card"></div>
<div class="abs contact-ribbon">Contact Informations</div>
<div class="abs contact-line"><span>800.555.0142</span>info@nine-parts.com</div>

<div class="abs nav-band"></div>
<nav class="abs main-nav">
  <span class="current">Home</span><span>The Story</span><span>Why 9parts.com</span><span>Are you eligible?</span><span>Members</span><span>Clients</span>
</nav>

<div class="abs hero" role="img" aria-label="Photo of a hand typing on a laptop keyboard"></div>

<section class="abs welcome">
  <h1>Welcome to <strong>nine-parts.com</strong></h1>
  <p>Lorem ipsum dolor sit amet, consectetur adipiscing elit. Aenean facilisis libero tempus velit sodales, ac tristique eros tempus. Nullam molestie sapien ac eleifend aliquet. Suspendisse felis mauris, auctor vitae lacinia blandit, congue eu mi. Duis vel metus sed lacus convallis lobortis at ut leo. Maecenas gravida ipsum enim, at mollis tellus tempor eget. Sed ut arcu et leo luctus porta quis et leo. Curabitur ac lorem neque. <a href="#">Read More...</a></p>
</section>
<div class="abs welcome-shadow"></div>

<div class="abs panel"></div>
<h2 class="abs section-title" style="top:479px">How Much Do I Have to Payback?</h2>
<div class="abs calc-field" style="left:153px">Enter Amount of Loan: $ ____________</div>
<div class="abs calc-field" style="left:404px">12 payments of:$ ____________ / month</div>
<div class="abs calc-field" style="left:676px">Total Paid Back:$____________</div>
<div class="abs calc-hint">Min $300-Max $700</div>
<div class="abs rule" style="top:559px"></div>
<div class="abs calc-notes">It's that easy!<br>Once approved you will receive a confirmation number and your creditor will be funded within 72 hours<br>*Need referral number to get actual calculations</div>
<div class="abs rule" style="top:625px"></div>

<h2 class="abs section-title" style="top:650px">One place for your bills. Paid.</h2>

<div class="abs feature" style="left:174px;top:702px">
  <h3><svg width="18" height="22" viewBox="0 0 18 22"><path d="M9 1a8 8 0 0 0-8 8c0 6 8 12 8 12s8-6 8-12a8 8 0 0 0-8-8z" fill="#4cb84a"/><circle cx="9" cy="9" r="3" fill="#fff"/></svg>Easy &amp; organized just for you.</h3>
  <p>Morbi ornare convallis sollicitudin. Mauris diam enim, bibendum placerat justo ac, tempor rutrum justo. Sed semper ac tellus ut ultricies. Praesent dolor diam</p>
</div>
<div class="abs feature" style="left:527px;top:702px">
  <h3><svg width="32" height="22" viewBox="0 0 32 22"><g stroke="#9a9a9a" stroke-width="1.5"><line x1="1" y1="8" x2="11" y2="8"/><line x1="3" y1="12" x2="12" y2="12"/><line x1="1" y1="16" x2="10" y2="16"/></g><circle cx="25" cy="3.5" r="3" fill="#4cb84a"/><path d="M14 11l6-5 5 3-3 5 4 6M20 6l-6 9-3 5M25 9l4 3" stroke="#4cb84a" stroke-width="2.4" fill="none" stroke-linecap="round"/></svg>Faster than a speeding bullet.</h3>
  <p>Morbi ornare convallis sollicitudin. Mauris diam enim, bibendum placerat justo ac, tempor rutrum justo. Sed semper ac tellus ut ultricies. Praesent dolor diam</p>
</div>
<div class="abs feature" style="left:174px;top:827px">
  <h3><svg width="20" height="20" viewBox="0 0 20 20"><circle cx="10" cy="10" r="10" fill="#4cb84a"/><path d="M9 5v6h5" stroke="#fff" stroke-width="2" fill="none"/></svg>Real-time alerts and reminders.</h3>
  <p>Morbi ornare convallis sollicitudin. Mauris diam enim, bibendum placerat justo ac, tempor rutrum justo. Sed semper ac tellus ut ultricies. Praesent dolor diam</p>
</div>
<div class="abs feature" style="left:527px;top:827px">
  <h3><svg width="22" height="20" viewBox="0 0 22 20"><path d="M11 1L1 10h3v9h14v-9h3z" fill="#4cb84a"/><rect x="8" y="11" width="6" height="6" fill="#fff"/></svg>Security and peace of mind.</h3>
  <p>Morbi ornare convallis sollicitudin. Mauris diam enim, bibendum placerat justo ac, tempor rutrum justo. Sed semper ac tellus ut ultricies. Praesent dolor diam</p>
</div>

<section class="abs payees">
  <h2>Who Else Can I Pay?</h2>
  <div class="payee-types">
    <div><svg width="31" height="31" viewBox="0 0 31 31"><circle cx="15.5" cy="15.5" r="14" fill="none" stroke="#fff" stroke-width="2"/><path d="M15 8c-3 5-5 7-5 10a5 5 0 0 0 10 0c0-3-2-5-5-10z" fill="#fff"/></svg>Utilities</div>
    <div><svg width="31" height="31" viewBox="0 0 31 31"><circle cx="15.5" cy="15.5" r="14" fill="none" stroke="#fff" stroke-width="2"/><path d="M12 7v5M19 7v5M10 12h11v4a5.5 5.5 0 0 1-11 0zM15.5 21v5" stroke="#fff" stroke-width="2" fill="#fff"/></svg>Cable</div>
    <div><svg width="31" height="31" viewBox="0 0 31 31"><rect x="2" y="2" width="16" height="27" rx="2" fill="none" stroke="#fff" stroke-width="2"/><path d="M10 12h10v-5l10 9-10 9v-5h-10z" fill="#fff"/></svg>Cell Phone</div>
    <div><svg width="36" height="31" viewBox="0 0 36 31"><path d="M9 4h18l5 11H4z" fill="none" stroke="#fff" stroke-width="2"/><rect x="2" y="14" width="32" height="10" rx="2" fill="#fff"/><rect x="4" y="23" width="6" height="5" fill="#fff"/><rect x="26" y="23" width="6" height="5" fill="#fff"/><circle cx="8" cy="19" r="2" fill="#9bdd7e"/><circle cx="28" cy="19" r="2" fill="#9bdd7e"/></svg>Insurance</div>
  </div>
  <p class="payee-list">Arcline, Tellora, Skyplate TV, Timberwave, Coveline, Westgrid Power, Homestead Mutual, Northstar Assurance, Veridian Mobile, Sunbelt Electric, Coastal Light &amp; Power, Lakeshore Energy, Fieldmark, Keystone Shield, Allharbor, Corecast, Brightdish, Chartwell Cable, Quarrylink, Clearview Cable, Meridian Telecom, Swiftcell, and thousands more.</p>
</section>

<footer class="abs site-footer">
  <div class="footer-nav">Home | The Story | Why 9parts.com | Are you eligible? | Members | Clients</div>
  <div class="copyright">©2014 nine-parts.com. All rights reserved</div>
  <div class="social"><span></span><span></span><span></span></div>
</footer>

</body>
</html>
```